Velqora new official website

We need a new design for our website www.velqora-example.com We are web marketing publishers and our website must be attractive for clients. That's why we need to "refresh" it. The main colour of our logo is orange, and this is an indication for the colours of the website too. We need the design for the homepage and the design of inner pages. Here is the list of the various sections of the website:
- ABOUT US: Who we are/Certificates/Offices/Team
- SERVICES: SEM/Display/Email Marketing and coregistration/ad networking
- PROJECTS/NETWORK/BRANDS: We need one page per country with screenshots of the websites and very short descriptions.
- VELQORA & CHARITY
- WORK WITH US
- CONTACT US
- NEWS

```html
<!DOCTYPE html>
<html lang="en">
<head>
<meta charset="utf-8">
<title>Velqora – Web Marketing Publishers</title>
<link rel="stylesheet" href="https://fonts.googleapis.com/css2?family=Arimo:wght@400;700&display=swap">
<style>
:root{
  --orange:#f7931e;
  --orange-deep:#e8730f;
  --orange-light:#fbb040;
  --orange-pale:#fcc66a;
  --text:#3a3a3a;
  --muted:#8a8a8a;
  --rule:#d6d6d6;
  --dark:#262626;
  --white:#ffffff;
}
*{margin:0;padding:0;box-sizing:border-box}
html,body{width:1200px;height:900px;overflow:hidden;background:var(--white)}
body{font-family:"Arimo",Arial,sans-serif;color:var(--text);position:relative}
.abs{position:absolute}
.page{position:absolute;left:319px;top:0;width:527px;height:900px;background:var(--white)}
.topbar{left:0;top:0;width:527px;height:17px;background:linear-gradient(var(--orange-deep),#ef8a1c)}
.logo{left:60px;top:36px;display:flex;align-items:center;gap:3px;font-weight:700;font-size:15px;color:var(--orange-deep);letter-spacing:-.3px}
.logo-dot{width:11px;height:11px;border-radius:50%;background:var(--orange-deep)}
.subscribe{left:343px;top:26px;font-size:5.5px;color:var(--muted);display:flex;align-items:center;gap:3px}
.subscribe b{color:var(--orange)}
.rss{width:7px;height:7px;background:var(--orange);border-radius:1px}
.search-input{left:294px;top:52px;width:131px;height:14px;border:1px solid #9a9a9a;font-size:5.5px;padding:3px 5px;color:#333;background:#fff}
.search-btn{left:428px;top:52px;width:42px;height:14px;background:#4a4a4a;color:#fff;font-size:6.5px;text-align:center;line-height:14px}
.nav{left:0;top:70px;width:527px;height:38px;background:linear-gradient(var(--orange-pale),var(--orange) 55%,var(--orange-light))}
.nav a{position:absolute;top:18px;font-size:5px;font-weight:700;color:#fff;text-decoration:none;text-transform:uppercase;white-space:nowrap}
.nav .active-bg{position:absolute;left:108px;top:0;width:38px;height:38px;background:rgba(255,255,255,.18)}
.slider{left:64px;top:122px;width:399px;height:123px}
.tab{position:absolute;top:0;width:14px;height:123px;background:var(--orange);border-right:1px solid #ffd08a}
.tab span{position:absolute;left:50%;top:50%;transform:translate(-50%,-50%) rotate(-90deg);white-space:nowrap;color:#fff;font-size:5.5px}
.hero{position:absolute;left:44px;top:0;width:340px;height:123px;background:linear-gradient(100deg,#4b4440 0%,#8a8480 35%,#d9d6d2 70%,#efefef 100%)}
.hero-title{position:absolute;right:8px;top:84px;text-align:left;color:#333;font-size:9px;line-height:1}
.hero-title small{font-size:5px;display:block;margin-left:24px}
.hero-title strong{font-size:15px;font-weight:400;color:var(--orange)}
h2{font-size:10px;font-weight:700;color:var(--orange);position:absolute}
p.body{position:absolute;font-size:5px;line-height:9px;color:var(--text)}
.hr{left:57px;top:351px;width:413px;height:1px;background:var(--rule)}
.vr{left:273px;top:370px;width:1px;height:340px;background:var(--rule)}
.field{position:absolute;left:74px;width:160px;font-size:5px;line-height:9px}
.field h3{font-size:5px;font-weight:700;color:var(--orange)}
.field .more{color:var(--orange);text-decoration:underline}
.btn{position:absolute;height:10px;padding:0 4px;background:var(--orange);color:#fff;font-size:5px;line-height:10px;border-radius:2px}
.news-photo{left:289px;top:383px;width:88px;height:53px;background:linear-gradient(#3a2f2a,#8a3a30 60%,#5a4a44)}
.news-list{left:287px;top:446px;list-style:none}
.news-list li{display:flex;align-items:center;gap:7px;height:12.3px;font-size:5.5px;color:#444}
.news-list li span{border-bottom:1px solid #ccc;padding-bottom:1px}
.bullet{width:5px;height:5px;border-radius:50%;border:1px solid #999}
.adtech{position:absolute;left:288px;width:170px;font-size:4.6px;line-height:9px}
.adtech h3{font-size:4.8px;font-weight:700;color:var(--orange)}
.partners{left:72px;top:627px;width:185px;height:68px;border:3px solid var(--orange);border-radius:5px;background:var(--orange)}
.partners-inner{position:absolute;left:2px;top:2px;width:175px;height:46px;background:#fff;border-radius:3px;display:flex;align-items:center;gap:5px;padding:0 6px}
.badge{background:#ddd;border-radius:2px}
.partners p{position:absolute;left:4px;top:50px;font-size:4.2px;line-height:8px;color:#fff}
.footer{left:0;top:715px;width:527px;height:135px;background:var(--orange)}
.fcol{position:absolute;top:18px;color:#fff}
.fcol h4{font-size:9px;font-weight:400;display:flex;align-items:center;gap:8px;margin-bottom:12px}
.arrow{width:6px;height:6px;border-radius:50%;background:#fff;position:relative}
.arrow::after{content:"";position:absolute;left:2px;top:1.5px;border-left:2px solid var(--orange);border-top:1.5px solid transparent;border-bottom:1.5px solid transparent}
.fcol p{font-size:5px;line-height:8.5px}
.fcol em{font-style:italic}
.form-row{display:flex;align-items:center;gap:6px;margin-top:4px;font-size:5px}
.form-row label{width:42px;padding-left:6px}
.form-row input{width:83px;height:13px;border:1px solid #ccc;border-radius:2px;background:linear-gradient(#eee,#fff)}
.submit{margin:4px 0 0 83px;width:53px;height:12px;background:#1f1f1f;color:#fff;font-size:5.5px;text-align:center;line-height:12px;border-radius:2px}
.bottom{left:0;top:850px;width:527px;height:50px;background:var(--dark);color:#fff;text-align:center;font-size:5px}
.bottom nav{margin-top:7px}
.bottom nav a{color:#fff;text-decoration:none}
.bottom p{margin-top:4px;line-height:8px}
</style>
</head>
<body>
<div class="page">
  <div class="abs topbar"></div>

  <header>
    <div class="abs logo"><span>velqora</span><span class="logo-dot"></span></div>
    <div class="abs subscribe"><span class="rss"></span><b>Please subscribe</b> to: Posts | Comments | Email</div>
    <div class="abs search-input">Type here...</div>
    <div class="abs search-btn">Search</div>
  </header>

  <nav class="abs nav">
    <span class="active-bg"></span>
    <a style="left:116px">About us</a>
    <a style="left:153px">Services</a>
    <a style="left:188px">Projects / Network / Brands</a>
    <a style="left:275px">Velqora</a>
    <a style="left:310px">Work with us</a>
    <a style="left:358px">Contact us</a>
    <a style="left:400px">News</a>
  </nav>

  <section class="abs slider">
    <div class="tab" style="left:0"><span>Slide 1 Lorem ipsum dolor sit amet</span></div>
    <div class="tab" style="left:14px"><span>Slide 2 Advertising Consectetur</span></div>
    <div class="tab" style="left:28px"><span>Slide 3 Lorem ipsum dolor sit amet</span></div>
    <div class="hero" role="img" aria-label="Photo of a businessman at a boardroom table with a globe, silhouettes of business people on the right">
      <div class="hero-title">THE MAIN WAY<small>TO YOUR</small><strong>BUSINESS</strong></div>
    </div>
    <div class="tab" style="left:385px;border:0"><span>Slide 4 Lorem ipsum dolor sit amet</span></div>
  </section>

  <h2 style="left:73px;top:275px">Scope and Mission</h2>
  <p class="body" style="left:73px;top:294px;width:190px">Our aim is creating adding value on our customers sales through technology and web marketing by means of the most modern web advertising systems. We help our customers in developing new sales strategies based on the web marketing. We watch the market and support our customers in achieving excellent visibility on the newest advertising channels. We are able to offer a wide range of either standard or tailored solutions.</p>

  <h2 style="left:276px;top:275px">Clients' strategies and web know how</h2>
  <p class="body" style="left:276px;top:294px;width:195px">We cooperate with the MAIN international brands in the fields of tourism, finance, fashion, durable goods, technologies &amp; communication. We help our customers in finding the way to succeed on every single one of their campaigns and on the brand awareness. We implement our strategies also in cooperation with some well known international partners who cooperate with us in tracing and checking statistics and performances.</p>

  <div class="abs hr"></div>
  <div class="abs vr"></div>

  <h2 style="left:74px;top:369px">Fields of Expertise</h2>
  <div class="field" style="top:386px"><h3>Tourism</h3>Tourism has been our first passion.Today it is our MAIN business and generates our MAIN income.<br><span class="more">» READ MORE</span></div>
  <div class="field" style="top:430px"><h3>Technologies &amp; Communication</h3>Dvd, lap tops, hardware, isn't that a hard job to keep updated about it?<br><span class="more">» READ MORE</span></div>
  <div class="field" style="top:466px"><h3>Finance</h3>VELQORA has been working for a long time with the MAIN brands in the international world of finance.<br><span class="more">» READ MORE</span></div>
  <div class="field" style="top:510px"><h3>Fashion</h3>The new frontier for our company is the world of fashion; We believe that today, television and the internet are merging.<br><span class="more">» READ MORE</span></div>
  <div class="field" style="top:554px"><h3>Durable Goods</h3>As publisher we help the MAIN brands in the field of automotive, appliances, business equipment ...<br><span class="more">» READ MORE</span></div>
  <div class="btn" style="left:74px;top:596px">Read More</div>

  <h2 style="left:288px;top:369px">Velqora News</h2>
  <div class="abs news-photo" role="img" aria-label="Photo of a crowded trade fair hall"></div>
  <ul class="abs news-list">
    <li><span class="bullet"></span><span>Simply dummy text of the printing and typesetting industry.</span></li>
    <li><span class="bullet"></span><span>Lorem has been the industry's standard dummy text.</span></li>
    <li><span class="bullet"></span><span>Ever since thes, when an unknown printer.</span></li>
    <li><span class="bullet"></span><span>Has been the industry's standard dummy text ever since thes.</span></li>
    <li><span class="bullet"></span><span>Simply dummy text of the printing and typesetting industry.</span></li>
    <li><span class="bullet"></span><span>Lorem Ipsum has been the industry's standard dummy text.</span></li>
    <li><span class="bullet"></span><span>Ever since thes when an unknown printer.</span></li>
  </ul>
  <div class="btn" style="left:287px;top:537px">Read More</div>

  <h2 style="left:288px;top:561px">Adtech News</h2>
  <div class="adtech" style="top:577px"><h3>The Role of On-Page SEO Content: Relevance, Not Rankings</h3>From an SEO perspective, on-page content is solely about helping establish what search queries your page might be relevant to. ...</div>
  <div class="adtech" style="top:613px"><h3>Harlow Grid Is About To Change Marketplace... Again.</h3>Harlow Grid begins beta-testing of a new inventory and delivery system for Marketplace. ...</div>
  <div class="adtech" style="top:648px"><h3>Bidder Beware: What You Need to Know When Updating Searchly Ads Bid Types</h3>Max CPC, Enhanced CPC, Automatic Bidding, Conversion Optimizer — each Searchly Ads bidding option carries a distinct set of pros ...</div>
  <div class="btn" style="left:287px;top:687px">Read More</div>

  <div class="abs partners">
    <div class="partners-inner">
      <div class="badge" style="width:34px;height:40px;background:var(--orange)"></div>
      <div class="badge" style="width:38px;height:24px"></div>
      <div class="badge" style="width:24px;height:26px"></div>
      <div class="badge" style="width:30px;height:22px"></div>
      <div class="badge" style="width:20px;height:20px;border-radius:50%"></div>
    </div>
    <p>VELQORA, Via Orsolina 14 - 00100 Terralto (TR) Italy Group, Tel.+39 000 0000000<br>Fax +39 000 0000000 VAT IT 00000000000</p>
  </div>

  <footer class="abs footer">
    <div class="fcol" style="left:68px;width:108px">
      <h4><span class="arrow"></span>Testimonials</h4>
      <p><em>"Lorem Ipsum is simply dummy text of the printing and typesetting industry. Lorem Ipsum has been the industry's standard and ever since the 1500s, when an unknown printer dummy..."</em></p>
    </div>
    <div class="fcol" style="left:194px;width:140px">
      <h4><span class="arrow"></span>Newsletter</h4>
      <p>Duis aute irure dolor in reprehenderit in voluptate velit esse cillum dolore eu fugiat nulla pariatur.</p>
      <div class="form-row"><label>Your Name</label><input type="text" aria-label="Your Name"></div>
      <div class="form-row"><label>Your Email Address</label><input type="text" aria-label="Your Email Address"></div>
      <div class="submit">Submit</div>
    </div>
    <div class="fcol" style="left:346px;width:130px">
      <h4><span class="arrow"></span>Contact us</h4>
      <p>HEAD OFFICE: Velqora srl - Via Orsolina 14<br>00100 Terralto (TR) - ITALY<br>Tel +39 000 0000000 Fax +39 000 0000000<br>BRANCH OFFICE: 17 Linden Road, Northgate<br>000000 Northgate - INDIA<br>BRANCH OFFICE: Harbour House, Eastmere Road<br>tel 000 0000000 Westvale - INDIA<br>BRANCH OFFICE: Travessera de Sol 10, 2-1</p>
    </div>
  </footer>

  <div class="abs bottom">
    <nav><a>HOME</a> | <a>ABOUT US</a> | <a>WORK WITH US</a> | <a>OUR SITES</a> | <a>GET YOUR QUOTE</a> | <a>WEB MASTER</a> | <a>NEWS LETTER</a> | <a>CONTACT US</a></nav>
    <p>© Copyright 2011. www.velqora-example.com. All Rights Reserved</p>
  </div>
</div>
</body>
</html>
```